Business Card Design - Law Firm

We are a boutique law firm located near the beach in Manly, Australia. We have recently had a new logo designed and are revamping our business cards with the new logo.

We have recently had a business card design done for us but are not entirely happy with it. We are looking for something modern, simplistic but striking. We would like to see multiple designs.

We have attached a word document which includes our new logo and the current business card design which we are looking at moving away from.

We would like the business cards to be double sided. We would like the design to include something which we can print in gloss colour when we send it to the business card printers.

```html
<!DOCTYPE html>
<html lang="en">
<head>
<meta charset="utf-8">
<title>Halden &amp; Partners Lawyers – Business Card</title>
<link rel="stylesheet" href="https://fonts.googleapis.com/css2?family=Raleway:wght@500;600;700&display=swap">
<style>
  :root {
    --backdrop: #d8d3cb;
    --card: #eeeeee;
    --navy: #2e3f8f;
    --gold: #b3a46c;
    --ink: #1a1a1a;
  }
  * { margin: 0; padding: 0; box-sizing: border-box; }
  html, body { width: 900px; height: 1200px; overflow: hidden; }
  body {
    background: var(--backdrop);
    font-family: "Raleway", sans-serif;
    color: var(--ink);
    position: relative;
  }
  .card {
    position: absolute;
    background: var(--card);
    box-shadow: 0 6px 18px rgba(0,0,0,0.18);
  }
  /* Front side */
  .card-front { left: 64px; top: 130px; width: 779px; height: 440px; }
  .rule { position: absolute; background: var(--gold); }
  .rule-vertical { left: 259px; top: 70px; width: 3px; height: 300px; }
  .rule-horizontal { left: 69px; top: 163px; width: 643px; height: 3px; }
  .front-brand {
    position: absolute; left: 86px; top: 88px;
    display: flex; align-items: center; gap: 8px;
  }
  .brand-dot { width: 16px; height: 16px; border-radius: 50%; background: var(--navy); }
  .front-brand .brand-name { font-size: 13px; font-weight: 700; color: var(--navy); }
  .person { position: absolute; left: 313px; top: 82px; }
  .person-name { font-size: 24px; font-weight: 700; color: var(--navy); letter-spacing: 0.5px; line-height: 30px; }
  .person-role { font-size: 19px; font-weight: 500; letter-spacing: 0.8px; line-height: 26px; }
  .contact { position: absolute; left: 313px; top: 200px; font-size: 18.5px; font-weight: 500; letter-spacing: 0.6px; }
  .contact p { line-height: 31px; }
  .contact .web { font-weight: 700; }
  .address { margin-top: 18px; }
  .address p { line-height: 26px; }
  /* Back side */
  .card-back { left: 64px; top: 626px; width: 782px; height: 445px; }
  .frame { position: absolute; inset: 0; }
  .back-brand {
    position: absolute; left: 0; right: 0; top: 120px;
    display: flex; flex-direction: column; align-items: center; gap: 46px;
  }
  .brand-mark { width: 120px; height: 120px; border-radius: 50%; background: var(--navy); }
  .back-brand .brand-name { font-size: 29px; font-weight: 700; letter-spacing: 2px; color: var(--ink); }
</style>
</head>
<body>
  <section class="card card-front">
    <div class="front-brand">
      <span class="brand-dot"></span>
      <span class="brand-name">Halden &amp; Partners</span>
    </div>
    <div class="rule rule-vertical"></div>
    <div class="rule rule-horizontal"></div>
    <div class="person">
      <h1 class="person-name">Maren Holloway</h1>
      <p class="person-role">Practice Manager</p>
    </div>
    <div class="contact">
      <p>(02) 9410 3876</p>
      <p class="web">www.haldenpartners.com.au</p>
      <p>maren.holloway@haldenlaw.com.au</p>
      <div class="address">
        <p>Suite 4, 12 Collins Parade</p>
        <p>Freshwater NSW 2096</p>
      </div>
    </div>
  </section>

  <section class="card card-back">
    <svg class="frame" width="782" height="445" viewBox="0 0 782 445" aria-hidden="true">
      <rect x="0" y="0" width="782" height="445" fill="var(--gold)"/>
      <polygon points="0,0 590,0 572,19 19,19 19,426 205,426 186,445 0,445" fill="var(--navy)"/>
      <rect x="19" y="19" width="744" height="407" fill="var(--card)"/>
    </svg>
    <div class="back-brand">
      <span class="brand-mark"></span>
      <span class="brand-name">Halden &amp; Partners Lawyers</span>
    </div>
  </section>
</body>
</html>
```